Header Design

I would like a new header design for my website - www.nestmarlo.com.

I am a Realtor and the header should reflect that and complement the theme.

The attached logo needs to be included and the information that is already there. Also, the colors need to match.

Marlo Quinby
Connecting you to the Los Angeles real estate scene.

Industry/Entity Type

Realtor

```html
<!DOCTYPE html>
<html lang="en">
<head>
<meta charset="utf-8">
<title>Marlo Quinby – Los Angeles Real Estate</title>
<link rel="stylesheet" href="https://fonts.googleapis.com/css2?family=Italianno&family=Open+Sans:ital,wght@1,600&display=swap">
<style>
  :root {
    --frame: #3a2540;
    --white: #ffffff;
    --sky-top: #2f3d5c;
    --sky-mid: #5c6f8e;
    --dusk-glow: #e38a4a;
    --dusk-pink: #b9868f;
    --city-dark: #1a1620;
    --city-light: #3a2c2a;
  }
  html, body {
    margin: 0;
    padding: 0;
    overflow: hidden;
    background: var(--white);
  }
  .site-header {
    position: relative;
    width: 1200px;
    height: 125px;
    background: var(--frame);
    overflow: hidden;
  }
  .skyline-photo {
    position: absolute;
    left: 5px;
    top: 4px;
    width: 1080px;
    height: 115px;
    background: linear-gradient(
      to bottom,
      var(--sky-top) 0%,
      var(--sky-mid) 28%,
      var(--dusk-pink) 38%,
      var(--dusk-glow) 44%,
      var(--city-light) 52%,
      var(--city-dark) 100%
    );
  }
  .agent-name {
    position: absolute;
    left: 168px;
    top: 2px;
    margin: 0;
    font-family: "Italianno", cursive;
    font-weight: 400;
    font-size: 46px;
    letter-spacing: 3px;
    color: var(--white);
    word-spacing: 22px;
  }
  .tagline {
    position: absolute;
    left: 58px;
    top: 80px;
    margin: 0;
    font-family: "Open Sans", sans-serif;
    font-style: italic;
    font-weight: 600;
    font-size: 15px;
    color: var(--white);
  }
  .brand-mark {
    position: absolute;
    left: 1088px;
    top: 0;
    width: 112px;
    height: 125px;
    display: flex;
    flex-direction: column;
    align-items: center;
    justify-content: center;
    gap: 8px;
  }
  .brand-square {
    width: 30px;
    height: 30px;
    background: var(--white);
  }
  .brand-name {
    font-family: "Open Sans", sans-serif;
    font-style: italic;
    font-weight: 600;
    font-size: 12px;
    line-height: 1.2;
    text-align: center;
    color: var(--white);
  }
</style>
</head>
<body>
  <header class="site-header">
    <div class="skyline-photo" role="img" aria-label="Los Angeles city lights at dusk seen from the hills, orange glow on the horizon"></div>
    <h1 class="agent-name">Marlo Quinby</h1>
    <p class="tagline">Connecting you to the Los Angeles real estate scene.</p>
    <div class="brand-mark">
      <span class="brand-square"></span>
      <span class="brand-name">Marlo<br>Quinby</span>
    </div>
  </header>
</body>
</html>
```